Business Card Project for 'Manufacturing and Healthcare Business Improvement company.

I need a business card for a consulting company that does process improvement for manufacturing and healthcare companies. I had a contest for a logo, and I liked what we came up with for the logo.

I wasn't blown away by what I got for the business card. The designer tried and it was a decent design, but I was looking for a little more. I want something that looks professional, but is eye-catching enough that people say "that looks cool, where did you get it?"

I've uploaded some business card examples I found that I liked. Even though some of the examples have red and orange on them, I think I would stick with blues, grays and blacks since that matches the logo theme. As awesome as some of them look, I don't think that a single color card, like an all-black card, will work for me; but feel free to change my mind.

It might also be possible to incorporate elements from the logo into the card. I also like some of the elements that use circles or rectangles etc to separate the phone number, website etc.

I like it when people have used geometric shapes to break up the card into sections or to add borders to the card to complement the logo, not compete with it for attention. For example, the red and gray example that has a curve that separates the card into two parts. I've wondered, how it would look if the red area were blue and had an arrow separating the top and bottom, like the arrow on the logo. Maybe on the back there could be an element that mirrors the bar graph and arrow. Would those look interesting, or would they compete with the other elements too much?

I also uploaded some examples of cards I made up, either based on ideas I saw elsewhere or based on design elements that the logo had in his designs. If you wonder why the ones with "lorem ipsum" look like an amateur did them, it's because they did.

I also think that I may add a QR code at some point, so I would need a location for that, along with something that says what the QR links to, such as, "scan here to upload contact information" or something similar. I don't know if I want cards that require having special designs cut, but if you have the idea, go with it.

I don't want to limit anyone's creativity, so I'll leave it at that.

Target Market(s)

Healthcare and Manufacturing

Industry/Entity Type

Manufacturing

Contact Information for Business Card

Harborline Advisory Group LLC.
Owen Prescott MBA, LSSMBB
Managing Partner
o.prescott@harborlineadvisorygroupllc.com
(555) 987-2310

Font styles to use
Serif
Sans Serif

Colors

Designer to choose only greyscale colors for use in the design.

Requirements
Must have
• The logo.
Nice to have
• Even though some of the examples I uploaded have red and orange on them, I think I would stick with blues, grays and blacks since that matches the logo theme.

I also like some of the elements that use circles or rectangles etc to separate the phone number, website etc.

I like it when people have used geometric shapes to break up the card into sections or to add borders to the card to complement the logo, not compete with it for attention.

For example, the red and gray example that has a curve that separates the card into two parts. I've wondered, how it would look if the red area were blue and had an arrow separating the top and bottom, like the arrow on the logo. Maybe on the back there could be an element that mirrors the bar graph and arrow. Would those look interesting, or would they compete with the other elements too much?

It might also be possible to incorporate elements from the logo into the card.

I also think that I may add a QR code at some point, so I would need a location for that, along with something that says what the QR links to, such as, "scan here to upload contact information" or something similar.

It could have something somewhere saying "We use Lean, Six Sigma and TPM continuous improvement tools to improve manufacturing and healthcare businesses."
Should not have
• So many colors and elements that it is distracting. Should not be generic.

As awesome as some of them look, I don't think that a single color card, like an all-black card, will work for me; but feel free to change my mind.

I don't know if I want cards that require having special designs cut, but if you have the idea, go with it.

```html
<!DOCTYPE html>
<html lang="en">
<head>
<meta charset="utf-8">
<title>Harborline Advisory Group – Business Card</title>
<link rel="stylesheet" href="https://fonts.googleapis.com/css2?family=Montserrat:wght@300;400;600;700&family=Roboto+Condensed:wght@400;500&display=swap">
<style>
  :root {
    --backdrop: #000000;
    --bleed: #d6d6d6;
    --paper: #ffffff;
    --navy: #1d3564;
    --charcoal: #4a4a4c;
    --text-grey: #4a4a4c;
    --safe-line: #f2d43a;
    --trim-line: #5a5a5a;
  }
  * { margin: 0; padding: 0; box-sizing: border-box; }
  html, body { width: 1200px; height: 1200px; overflow: hidden; background: var(--backdrop); }
  .canvas { position: relative; width: 1200px; height: 1200px; }
  .card-art { position: absolute; left: 0; top: 0; }

  .wordmark {
    position: absolute;
    color: var(--navy);
    font-family: "Montserrat", sans-serif;
    font-weight: 600;
    text-align: center;
    line-height: 1.05;
    letter-spacing: 0.02em;
  }
  .wordmark--front { left: 440px; top: 318px; width: 320px; font-size: 34px; }
  .wordmark--front .wordmark__sub { display: block; font-size: 17px; margin-top: 8px; letter-spacing: 0.08em; }
  .wordmark--back { left: 400px; top: 728px; width: 170px; font-size: 20px; }
  .wordmark--back .wordmark__sub { display: block; font-size: 10px; margin-top: 5px; letter-spacing: 0.06em; }

  .person { position: absolute; left: 405px; top: 871px; width: 160px; text-align: center; color: var(--text-grey); font-family: "Montserrat", sans-serif; }
  .person__name { font-size: 14px; letter-spacing: 0.03em; font-weight: 300; white-space: nowrap; }
  .person__name strong { font-weight: 600; }
  .person__title { font-size: 9px; letter-spacing: 0.06em; margin-top: 1px; border-top: 1px solid var(--text-grey); display: inline-block; padding-top: 1px; }

  .contact { position: absolute; left: 665px; color: var(--text-grey); font-family: "Roboto Condensed", sans-serif; font-weight: 500; white-space: nowrap; }
  .contact--phone { top: 735px; font-size: 10px; line-height: 14px; }
  .contact--email { top: 778px; font-size: 12.5px; }
  .contact--web { top: 815px; font-size: 12px; }
  .contact--address { top: 850px; font-size: 12px; line-height: 13px; }
</style>
</head>
<body>
<div class="canvas">
  <svg class="card-art" width="1200" height="1200" viewBox="0 0 1200 1200">
    <!-- front card -->
    <g class="card card--front">
      <rect x="328" y="223" width="544" height="327" fill="var(--bleed)"/>
      <rect x="347" y="242" width="506" height="289" fill="var(--paper)"/>
      <polygon points="347,486 604,486 586,514 347,514" fill="var(--charcoal)"/>
      <polygon points="614,486 853,486 853,514 595,514" fill="var(--navy)"/>
      <rect x="364.5" y="261.5" width="470" height="252" fill="none" stroke="var(--safe-line)" stroke-width="0.8"/>
      <g stroke="var(--trim-line)" stroke-width="1" stroke-dasharray="3 2" fill="none">
        <line x1="347" y1="223" x2="347" y2="550"/>
        <line x1="853" y1="223" x2="853" y2="550"/>
        <line x1="328" y1="242" x2="872" y2="242"/>
        <line x1="328" y1="531" x2="872" y2="531"/>
      </g>
    </g>

    <!-- back card -->
    <g class="card card--back">
      <rect x="328" y="649" width="544" height="327" fill="var(--bleed)"/>
      <rect x="347" y="668" width="506" height="289" fill="var(--paper)"/>
      <polygon points="347,912 586,912 604,940 347,940" fill="var(--navy)"/>
      <polygon points="595,912 853,912 853,940 614,940" fill="var(--charcoal)"/>
      <rect x="365.5" y="686.5" width="470" height="252" fill="none" stroke="var(--safe-line)" stroke-width="0.8"/>
      <g stroke="var(--trim-line)" stroke-width="1" stroke-dasharray="3 2" fill="none">
        <line x1="347" y1="649" x2="347" y2="976"/>
        <line x1="853" y1="649" x2="853" y2="976"/>
        <line x1="328" y1="668" x2="872" y2="668"/>
        <line x1="328" y1="957" x2="872" y2="957"/>
      </g>

      <!-- contact icons -->
      <g class="icon icon--phone" transform="translate(638 749)">
        <circle r="14" fill="var(--navy)"/>
        <path d="M-6,-6 l3,-2 l3,4 l-2,2 q1,3 4,4 l2,-2 l4,3 l-2,3 q-8,1 -12,-12 z" fill="var(--paper)"/>
      </g>
      <g class="icon icon--mail" transform="translate(638 786)">
        <circle r="14" fill="var(--navy)"/>
        <rect x="-8" y="-5.5" width="16" height="11" fill="none" stroke="var(--paper)" stroke-width="1.5"/>
        <polyline points="-8,-5.5 0,1 8,-5.5" fill="none" stroke="var(--paper)" stroke-width="1.5"/>
        <line x1="-8" y1="5.5" x2="-2" y2="0" stroke="var(--paper)" stroke-width="1.2"/>
        <line x1="8" y1="5.5" x2="2" y2="0" stroke="var(--paper)" stroke-width="1.2"/>
      </g>
      <g class="icon icon--web" transform="translate(638 825)">
        <circle r="14" fill="var(--navy)"/>
        <g fill="none" stroke="var(--paper)" stroke-width="1.3">
          <circle r="8"/>
          <ellipse rx="3.5" ry="8"/>
          <line x1="-8" y1="0" x2="8" y2="0"/>
          <line x1="-7" y1="-4" x2="7" y2="-4"/>
          <line x1="-7" y1="4" x2="7" y2="4"/>
        </g>
      </g>
      <g class="icon icon--address" transform="translate(638 863)">
        <circle r="14" fill="var(--navy)"/>
        <polygon points="0,-8 -9,0 -6,0 -6,7 6,7 6,0 9,0" fill="var(--paper)"/>
        <rect x="-2" y="2" width="4" height="5" fill="var(--navy)"/>
      </g>
    </g>
  </svg>

  <div class="wordmark wordmark--front">HARBORLINE<span class="wordmark__sub">ADVISORY GROUP LLC.</span></div>
  <div class="wordmark wordmark--back">HARBORLINE<span class="wordmark__sub">ADVISORY GROUP LLC.</span></div>

  <div class="person">
    <div class="person__name"><strong>OWEN</strong> PRESCOTT</div>
    <div class="person__title">MANAGING PARTNER</div>
  </div>

  <div class="contact contact--phone">(555) 987-2310<br>(555) 987-2310</div>
  <div class="contact contact--email">Lorem@isum.com</div>
  <div class="contact contact--web">www.companyname.com</div>
  <div class="contact contact--address">First Address line<br>Second Address line</div>
</div>
</body>
</html>
```